Bright Meadow Medical Centers - website

Would like a multicultural website with pictures of physicians and nurses of all races interacting with patients of all races and ages from kids to seniors (in a medical practice) not a hospital.

Would like a page devoted to Pediatric Care, Adult/Family Care, Retirees/Senior Care. With a list of general primary care services for each page, including lab and transportation.
Updates

Target Market(s)

Adult medicine, Pediatric Medicine, Retiree/Senior Care

Industry/Entity Type

Health Care

Number of Pages Required

3 page

Font styles to use
Sans Serif

Requirements
Must have
• I like the website “lakewaybasiccare.com” in Atlanta.
• Prefer the design look and feel like this even though the services are very different.

```html
<!DOCTYPE html>
<html lang="en">
<head>
<meta charset="utf-8">
<title>Bright Meadow Medical Centers</title>
<link href="https://fonts.googleapis.com/css2?family=Oxygen:wght@300;400;700&display=swap" rel="stylesheet">
<style>
:root{
  --green:#56a231;
  --green-dark:#4a8f2a;
  --navy:#153a63;
  --navy-deep:#0f2e50;
  --ink:#333a40;
  --muted:#5c6166;
  --light:#f2f2f2;
  --footer:#232323;
  --field:#4a4a4a;
  --white:#fff;
}
*{margin:0;padding:0;box-sizing:border-box}
html,body{width:1200px;height:2817px;overflow:hidden}
body{position:relative;font-family:"Oxygen",Arial,sans-serif;color:var(--ink);background:var(--white)}
.abs{position:absolute}
/* top bar */
.topbar{left:0;top:0;width:1200px;height:38px;background:var(--green);color:var(--white);font-size:12px}
.topbar .item{top:0;height:38px;display:flex;align-items:center;gap:8px}
.topbar .social{top:12px;width:14px;height:14px;border-radius:50%;background:var(--white);opacity:.9}
.login{left:1002px;top:0;width:98px;height:38px;background:var(--navy);display:flex;align-items:center;justify-content:center;gap:7px;font-weight:700;font-size:12px}
/* header */
.brand{left:100px;top:52px;width:200px}
.brand .mark{width:26px;height:26px;background:var(--green);margin:0 0 4px 64px}
.brand .name{font-weight:700;font-size:21px;color:var(--navy);letter-spacing:.3px;line-height:1}
.brand .sub{font-weight:700;font-size:9px;color:var(--green);letter-spacing:.5px;margin:4px 0 0 36px}
.hours{left:822px;top:72px;display:flex;gap:12px;align-items:center}
.hours .lines{font-size:15px;line-height:22px}
.hours .week{color:var(--navy)}
.hours .sat{color:var(--green);font-size:14px}
/* nav */
.nav{left:0;top:147px;width:1200px;height:52px;background:var(--navy)}
.nav a{position:absolute;top:0;height:52px;line-height:52px;color:var(--white);font-size:11px;font-weight:700;text-decoration:none;letter-spacing:.3px}
.nav a.active{background:var(--green);padding:0 27px;left:100px;height:50px;top:0}
/* hero */
.hero{left:0;top:199px;width:1200px;height:541px;background:linear-gradient(100deg,#c9a590 0%,#e8ddd5 25%,#b98a7e 45%,#d7dbe3 65%,#9fb2d8 85%,#c6cde0 100%)}
.hero-band{left:0;top:334px;width:661px;height:128px;background:rgba(21,58,99,.82);color:var(--white);font-size:40px;font-weight:700;letter-spacing:1px;padding:38px 0 0 100px}
.hero .arrow{top:250px}
/* welcome */
.center{left:0;width:1200px;text-align:center}
.h2{font-size:31px;font-weight:700;color:var(--navy)}
.welcome-sub{top:852px;font-size:14px;color:var(--green)}
.welcome-text{left:100px;top:890px;width:1000px;text-align:center;font-size:12.5px;line-height:26px;color:var(--ink)}
.btn-read{left:530px;top:1005px;width:140px;height:41px;background:var(--navy);color:var(--white);font-size:13px;font-weight:700;display:flex;align-items:center;justify-content:center;gap:8px;border:1px solid #0c2747}
/* services */
.card{top:1200px;width:231px;height:385px}
.card .photo{position:absolute;left:0;top:0;width:231px;height:176px}
.card svg.shape{position:absolute;left:0;top:158px}
.card .icon{position:absolute;left:96px;top:152px;width:40px;height:40px;border-radius:50%;display:flex;align-items:center;justify-content:center}
.card .title{position:absolute;left:0;top:208px;width:231px;text-align:center;color:var(--white);font-size:20px}
.card .text{position:absolute;left:14px;top:244px;width:203px;text-align:center;color:var(--white);font-size:11px;line-height:20px}
.card .more{position:absolute;left:0;top:333px;width:231px;text-align:center;color:var(--white);font-size:12px;font-weight:700;display:flex;justify-content:center;gap:7px;align-items:center}
.green .icon{background:var(--green)}
.navy .icon{background:var(--navy)}
/* blog */
.blog{left:0;top:1625px;width:1200px;height:499px;background:var(--light)}
.post{top:1754px;width:304px}
.post .photo{width:304px;height:171px;position:relative}
.post .photo svg{position:absolute;left:0;bottom:0}
.post .title{margin-top:30px;font-size:15px;line-height:22px}
.post .excerpt{margin-top:9px;font-size:12px;line-height:22px;color:var(--ink)}
.post .date{margin-top:12px;font-size:12px;display:flex;gap:8px;align-items:center}
/* team */
.member{top:2272px;width:220px;text-align:center}
.member .avatar{width:117px;height:117px;border-radius:50%;margin:0 auto;border:2px solid #cfd4da}
.member .name{margin-top:23px;font-size:15px;font-weight:700;color:var(--green)}
.member .role{margin-top:3px;font-size:12px;color:var(--muted)}
.member.lead .avatar{border:3px solid var(--navy)}
.member.lead .name,.member.lead .role{color:var(--navy)}
/* footer */
.footer{left:0;top:2502px;width:1200px;height:315px;background:var(--footer);color:#bdbdbd}
.footer h4{position:absolute;font-weight:400;font-size:18px;color:var(--white)}
.field{position:absolute;background:var(--field);border:1px solid #5a5a5a;font-size:11px;color:#9a9a9a;padding:10px 12px}
.submit{position:absolute;left:100px;top:180px;width:90px;height:34px;background:var(--green);color:var(--white);font-size:12px;font-weight:700;display:flex;align-items:center;justify-content:center}
.links{position:absolute;font-size:13px;line-height:29px;color:#a9a9a9}
.about{position:absolute;left:900px;top:68px;width:210px;font-size:13px;line-height:26px;color:#8f8f8f}
.about .loc{color:var(--green);margin-top:8px}
.copy{position:absolute;left:100px;top:278px;font-size:12px;color:#9a9a9a}
.foot-social{position:absolute;top:268px;width:27px;height:27px;border-radius:50%;background:#8a8a8a}
</style>
</head>
<body>

<!-- top bar -->
<div class="abs topbar">
  <div class="abs item" style="left:100px">
    <svg width="12" height="12" viewBox="0 0 24 24"><path fill="#fff" d="M6.6 10.8a15.1 15.1 0 0 0 6.6 6.6l2.2-2.2a1 1 0 0 1 1-.25 11.4 11.4 0 0 0 3.6.57 1 1 0 0 1 1 1V20a1 1 0 0 1-1 1A17 17 0 0 1 3 4a1 1 0 0 1 1-1h3.5a1 1 0 0 1 1 1c0 1.25.2 2.45.57 3.57a1 1 0 0 1-.25 1z"/></svg>
    <span>111 111 1111</span>
  </div>
  <div class="abs item" style="left:238px">
    <svg width="11" height="13" viewBox="0 0 24 28"><path fill="#fff" d="M12 0a9 9 0 0 0-9 9c0 7 9 19 9 19s9-12 9-19a9 9 0 0 0-9-9zm0 12.5A3.5 3.5 0 1 1 12 5.5a3.5 3.5 0 0 1 0 7z"/></svg>
    <span>Address ipsum dolor sit amet,</span>
  </div>
  <span class="abs social" style="left:926px"></span>
  <span class="abs social" style="left:953px"></span>
  <div class="abs login">
    <svg width="13" height="13" viewBox="0 0 24 24"><circle cx="8" cy="8" r="5" fill="none" stroke="#fff" stroke-width="3"/><path d="M11.5 11.5 21 21M17 17l3-3" stroke="#fff" stroke-width="3"/></svg>
    LOGIN
  </div>
</div>

<!-- header -->
<div class="abs brand">
  <div class="mark"></div>
  <div class="name">BRIGHT MEADOW</div>
  <div class="sub">MEDICAL CENTERS</div>
</div>
<div class="abs hours">
  <svg width="28" height="28" viewBox="0 0 28 28"><circle cx="14" cy="14" r="11.5" fill="none" stroke="var(--navy-deep)" stroke-width="3.5"/><path d="M14 7v7h5" stroke="var(--navy-deep)" stroke-width="2.5" fill="none"/></svg>
  <div class="lines">
    <div class="week">Monday - Friday 9.00am – 6.00pm</div>
    <div class="sat">Saturday 8.30am -12.00 pm</div>
  </div>
</div>

<!-- navigation -->
<nav class="abs nav">
  <a class="active">HOME</a>
  <a style="left:226px">ABOUT US</a>
  <a style="left:350px">PAEDIATRIC CARE</a>
  <a style="left:520px">ADULT/FAMILY CARE</a>
  <a style="left:707px">RETIREES/SENIOR CARE</a>
  <a style="left:913px">CONTACT US</a>
</nav>

<!-- hero -->
<div class="abs hero" role="img" aria-label="Group photo of smiling physicians and nurses of diverse backgrounds">
  <svg class="abs arrow" style="left:30px" width="22" height="40" viewBox="0 0 22 40"><path d="M20 2 3 20l17 18" fill="none" stroke="#fff" stroke-width="2"/></svg>
  <svg class="abs arrow" style="left:1148px" width="22" height="40" viewBox="0 0 22 40"><path d="M2 2l17 18L2 38" fill="none" stroke="#fff" stroke-width="2"/></svg>
  <div class="abs hero-band">BRIGHT MEADOW MEDICAL</div>
</div>

<!-- welcome -->
<h1 class="abs center h2" style="top:795px">Welcome to Bright Meadow Medical</h1>
<p class="abs center welcome-sub">Bright Meadow Care Medical Centers is a new concept</p>
<p class="abs welcome-text">Bright Meadow Care Medical Centers is a new concep of providing comprehensive acute and chronic medical care in the same environment, with maintenance in continuity of care and physician- patient relationship. In short, it's like going to your own physician, who stays open seven days a week, with extended hours until nine at night, weekends and holidays, who treats acute problems such as injuries, cuts and bruises, cold symptoms and also treats chronic problems such as high blood pressure.</p>
<div class="abs btn-read">READ MORE
  <svg width="13" height="13" viewBox="0 0 14 14"><circle cx="7" cy="7" r="7" fill="#fff"/><path d="M5.5 4 8.5 7l-3 3" stroke="var(--navy)" stroke-width="2" fill="none"/></svg>
</div>

<!-- services -->
<h2 class="abs center h2" style="top:1112px">Our Services</h2>

<div class="abs card green" style="left:100px">
  <div class="photo" role="img" aria-label="Nurse caring for a baby" style="background:linear-gradient(120deg,#e9dcd2,#7d6a62 70%,#3c4a5e)"></div>
  <svg class="shape" width="231" height="227" viewBox="0 0 231 227"><path d="M0 20 Q115 -14 231 20 V196 Q174 232 116 210 Q58 188 0 208 Z" fill="var(--green)"/></svg>
  <div class="icon"><svg width="16" height="18" viewBox="0 0 16 18"><circle cx="8" cy="3" r="2.5" fill="#fff"/><path d="M2 6h12v2H10v9H8.8v-5H7.2v5H6V8H2z" fill="#fff"/></svg></div>
  <div class="title">Paediatric Care</div>
  <div class="text">We have more state of the art medical equipment than most medical so our patients don't have to drive all over town getting things from work.</div>
  <div class="more">VIEW MORE <svg width="12" height="12" viewBox="0 0 14 14"><circle cx="7" cy="7" r="7" fill="#fff"/><path d="M5.5 4 8.5 7l-3 3" stroke="var(--green)" stroke-width="2" fill="none"/></svg></div>
</div>

<div class="abs card navy" style="left:356px">
  <div class="photo" role="img" aria-label="Doctor greeting a mother and child" style="background:linear-gradient(120deg,#d9cfc6,#8a7a70 55%,#e6e6e6)"></div>
  <svg class="shape" width="231" height="227" viewBox="0 0 231 227"><path d="M0 20 Q115 -14 231 20 V196 Q174 232 116 210 Q58 188 0 208 Z" fill="var(--navy)"/></svg>
  <div class="icon"><svg width="18" height="14" viewBox="0 0 18 14"><circle cx="5" cy="3" r="2.5" fill="#fff"/><circle cx="13" cy="3" r="2.5" fill="#fff"/><circle cx="9" cy="7" r="2" fill="#fff"/><path d="M1 13c0-4 2-6 4-6s4 2 4 6zM9 13c0-4 2-6 4-6s4 2 4 6z" fill="#fff"/></svg></div>
  <div class="title">Family Care</div>
  <div class="text">We have more state of the art medical equipment than most medical so our patients don't have to drive all over town getting things from work.</div>
  <div class="more">VIEW MORE <svg width="12" height="12" viewBox="0 0 14 14"><circle cx="7" cy="7" r="7" fill="#fff"/><path d="M5.5 4 8.5 7l-3 3" stroke="var(--navy)" stroke-width="2" fill="none"/></svg></div>
</div>

<div class="abs card green" style="left:612px">
  <div class="photo" role="img" aria-label="Caregiver with a senior patient" style="background:linear-gradient(120deg,#cfc3b8,#e9e4de 45%,#8a99b0)"></div>
  <svg class="shape" width="231" height="227" viewBox="0 0 231 227"><path d="M0 20 Q115 -14 231 20 V196 Q174 232 116 210 Q58 188 0 208 Z" fill="var(--green)"/></svg>
  <div class="icon"><svg width="14" height="18" viewBox="0 0 14 18"><circle cx="7" cy="3" r="2.5" fill="none" stroke="#fff" stroke-width="1.5"/><path d="M4 17V8h6v9M10 10l3 7" fill="none" stroke="#fff" stroke-width="1.5"/></svg></div>
  <div class="title">Senior Care</div>
  <div class="text">We have more state of the art medical equipment than most medical so our patients don't have to drive all over town getting things from work.</div>
  <div class="more">VIEW MORE <svg width="12" height="12" viewBox="0 0 14 14"><circle cx="7" cy="7" r="7" fill="#fff"/><path d="M5.5 4 8.5 7l-3 3" stroke="var(--green)" stroke-width="2" fill="none"/></svg></div>
</div>

<div class="abs card navy" style="left:869px">
  <div class="photo" role="img" aria-label="Nurses attending a family in a clinic" style="background:linear-gradient(120deg,#c96a5a,#e7d8c8 50%,#6f8fb0)"></div>
  <svg class="shape" width="231" height="227" viewBox="0 0 231 227"><path d="M0 20 Q115 -14 231 20 V196 Q174 232 116 210 Q58 188 0 208 Z" fill="var(--navy)"/></svg>
  <div class="icon"><svg width="18" height="16" viewBox="0 0 18 16"><path d="M4 3h10l-1 3H5z" fill="#fff"/><circle cx="9" cy="8" r="2.5" fill="#fff"/><path d="M3 16c0-3 3-5 6-5s6 2 6 5z" fill="#fff"/></svg></div>
  <div class="title">Physicians &amp; Nurses</div>
  <div class="text">We have more state of the art medical equipment than most medical so our patients don't have to drive all over town getting things from work.</div>
  <div class="more">VIEW MORE <svg width="12" height="12" viewBox="0 0 14 14"><circle cx="7" cy="7" r="7" fill="#fff"/><path d="M5.5 4 8.5 7l-3 3" stroke="var(--navy)" stroke-width="2" fill="none"/></svg></div>
</div>

<!-- blog -->
<section class="abs blog"></section>
<h2 class="abs center h2" style="top:1674px">Our Blog</h2>

<article class="abs post" style="left:100px">
  <div class="photo" role="img" aria-label="Smiling doctor in a bright clinic" style="background:linear-gradient(110deg,#b9ccd9,#e3e9ee 55%,#9fb5c6)">
    <svg width="304" height="22" viewBox="0 0 304 22"><path d="M0 22V10Q80 -4 160 12T304 4V22Z" fill="var(--light)"/></svg>
  </div>
  <div class="title" style="color:var(--navy)">Bright Meadow Care Medical Centers<br>is a new concept</div>
  <div class="excerpt">In short, it's like going to your own physician, who stays open seven days a week, until nine at night,[...]</div>
  <div class="date" style="color:var(--navy)"><svg width="13" height="13" viewBox="0 0 14 14"><rect x="1" y="2.5" width="12" height="10.5" fill="none" stroke="var(--navy)" stroke-width="1.5"/><path d="M1 5.5h12M4 1v3M10 1v3" stroke="var(--navy)" stroke-width="1.5"/></svg>11 Nov 2017</div>
</article>

<article class="abs post" style="left:449px">
  <div class="photo" role="img" aria-label="Doctor working at a laptop" style="background:linear-gradient(110deg,#2f3a44,#6c7a86 50%,#dfe3e6)">
    <svg width="304" height="22" viewBox="0 0 304 22"><path d="M0 22V10Q80 -4 160 12T304 4V22Z" fill="var(--light)"/></svg>
  </div>
  <div class="title" style="color:var(--green)">Bright Meadow Care Medical Centers<br>is a new concept</div>
  <div class="excerpt">In short, it's like going to your own physician, who stays open seven days a week, until nine at night,[...]</div>
  <div class="date" style="color:var(--green)"><svg width="13" height="13" viewBox="0 0 14 14"><rect x="1" y="2.5" width="12" height="10.5" fill="none" stroke="var(--green)" stroke-width="1.5"/><path d="M1 5.5h12M4 1v3M10 1v3" stroke="var(--green)" stroke-width="1.5"/></svg>11 Nov 2017</div>
</article>

<article class="abs post" style="left:798px">
  <div class="photo" role="img" aria-label="Doctor talking with a mother and daughter" style="background:linear-gradient(110deg,#e8e2dc,#c47a86 40%,#6e8fb8 75%,#efeae4)">
    <svg width="304" height="22" viewBox="0 0 304 22"><path d="M0 22V10Q80 -4 160 12T304 4V22Z" fill="var(--light)"/></svg>
  </div>
  <div class="title" style="color:var(--green)">Bright Meadow Care Medical Centers<br>is a new concept</div>
  <div class="excerpt">In short, it's like going to your own physician, who stays open seven days a week, until nine at night,[...]</div>
  <div class="date" style="color:var(--green)"><svg width="13" height="13" viewBox="0 0 14 14"><rect x="1" y="2.5" width="12" height="10.5" fill="none" stroke="var(--green)" stroke-width="1.5"/><path d="M1 5.5h12M4 1v3M10 1v3" stroke="var(--green)" stroke-width="1.5"/></svg>11 Nov 2017</div>
</article>

<!-- team -->
<h2 class="abs center h2" style="top:2184px">Meet Our Team</h2>
<svg class="abs" style="left:44px;top:2330px" width="14" height="28" viewBox="0 0 14 28"><path d="M13 1 2 14l11 13" fill="none" stroke="#c4c8cc" stroke-width="2"/></svg>
<svg class="abs" style="left:1130px;top:2330px" width="14" height="28" viewBox="0 0 14 28"><path d="M1 1l11 13L1 27" fill="none" stroke="#c4c8cc" stroke-width="2"/></svg>

<div class="abs member lead" style="left:48px">
  <div class="avatar" role="img" aria-label="Portrait of a team member" style="background:linear-gradient(#e9e3de,#c9a994)"></div>
  <div class="name">Nemo enim</div><div class="role">Ipsum dolor sit ame</div>
</div>
<div class="abs member" style="left:269px">
  <div class="avatar" role="img" aria-label="Portrait of a team member" style="background:linear-gradient(#e8e8e8,#6b4a3c)"></div>
  <div class="name">Ipsum dolor</div><div class="role">Nemo enim ipsam</div>
</div>
<div class="abs member" style="left:491px">
  <div class="avatar" role="img" aria-label="Portrait of a team member" style="background:linear-gradient(#e6e2de,#b08a74)"></div>
  <div class="name">Ipsum dolor</div><div class="role">Nemo enim ipsam</div>
</div>
<div class="abs member" style="left:711px">
  <div class="avatar" role="img" aria-label="Portrait of a team member" style="background:linear-gradient(#8e9aa6,#d4b6a4)"></div>
  <div class="name">Ipsum dolor</div><div class="role">Nemo enim ipsam</div>
</div>
<div class="abs member" style="left:932px">
  <div class="avatar" role="img" aria-label="Portrait of a team member" style="background:linear-gradient(#ecebea,#7a5a48)"></div>
  <div class="name">Ipsum dolor</div><div class="role">Nemo enim ipsam</div>
</div>

<!-- footer -->
<footer class="abs footer">
  <h4 style="left:100px;top:34px">Contact us</h4>
  <div class="field" style="left:100px;top:82px;width:202px;height:32px">Name</div>
  <div class="field" style="left:317px;top:82px;width:203px;height:32px">Email Address</div>
  <div class="field" style="left:100px;top:131px;width:202px;height:32px">Phone No</div>
  <div class="field" style="left:317px;top:131px;width:203px;height:62px">Messages</div>
  <div class="submit">SUBMIT</div>

  <h4 style="left:569px;top:34px">Quick Links</h4>
  <div class="links" style="left:569px;top:64px">Home<br>About us<br>Paediatric Care<br>Adult/Family Care</div>
  <div class="links" style="left:717px;top:64px">Retirees/Senior Care<br>Contact us</div>

  <h4 style="left:900px;top:34px">Bright Meadow Medical Centers</h4>
  <div class="about">We have been a model practice of the future of healthcare expand to all 50 states.
    <div class="loc">Location Details + Get Directions+</div>
  </div>

  <div class="copy">Copy Right ©2017 Bright Meadow. All Rights Reserved.</div>
  <span class="foot-social" style="left:997px"></span>
  <span class="foot-social" style="left:1033px"></span>
  <span class="foot-social" style="left:1070px"></span>
</footer>

</body>
</html>
```